Create a Brochure Design for Harlow Senior Living

Harlow Senior Living is a subsidiary of the Harlow Care Group. This brochure is specifically for the Harlow Senior Living company and brand. Create a 3 panel, front and back, tri-fold brochure. This brochure will be a way to introduce our senior living care home to the community, prospective, clients, and various referral partners. It is modern and state of the art home. Like the home, the brochure must be eye catching, unique in its deliverables (as it doesn’t feel like a care facility) and demonstrate both attention to detail and comfort. Our organization is sophisticated and built around warmth, care and individualized personal attention. The most important aspect of this design is to focus on creating a nurturing, warm, and inviting feel where you would want to put your own loved ones in our care home.
I am open to the creativity of the designer to develop something based on the above criteria; however I would like the design to work well with the existing collateral material. What I mean by that is that while I want everything to have its own personality and stand out as its own brand representative, I still need to be able to tell that the overall design concept stays stylistically inside of the same ‘family’ of existing designed material. Because of this, below I would like for the designer to pull inspiration from the link to our website (Located below) as well as from the attachment of our recently refreshed business cards (Attached). This should allow each design to be unique and creative, while still staying inside of a framework and the feel/style that I am looking for.
Finally, I want all the designers to understand that this brochure design is for a facility where we are responsible to provide care for active, positive, and happy seniors/elders. We have care professionals and staff on-site to provide 24x7, around the clock, care to the elders and geriatric residents as it is needed and required. The photos that are used must represent aging gracefully and with elegance.
Target Market(s)
Seniors(50+), Caring Family Members, Social Workers, Physicians, Hospitals
Industry/Entity Type
Business
Requirements
Must have
- • The company logo must be included.
Nice to have
- Attached you will find a sampling of images related to the long term care industry. Please feel free to use your own images as you see fit. The interior care home pictures are of our actual facility and should be incorporated into the brochure and your design.
Company Information
• Look under the Harlow Senior Living tab at
www.harlowcaregroup.example.

```html
<!DOCTYPE html>
<html lang="en">
<head>
<meta charset="utf-8">
<title>Harlow Senior Living – Tri-fold Brochure</title>
<link rel="stylesheet" href="https://fonts.googleapis.com/css2?family=Open+Sans:ital,wght@0,400;0,600;0,700;0,800;1,400&display=swap">
<style>
:root{
  --teal:#3f9c9a;
  --teal-dark:#2e7f7d;
  --plum:#7b1f5b;
  --sand:#d9c9bd;
  --paper:#f3f2f0;
  --ink:#3a3a3a;
  --rust:#8e1c1c;
  --fee:#f1dc8c;
  --fee-line:#d8bd5a;
  --slate:#5b5b5d;
  --stage:#6f6f6f;
}
*{box-sizing:border-box;margin:0;padding:0}
html,body{width:849px;height:1200px;overflow:hidden}
body{background:var(--stage);font-family:"Open Sans",Arial,sans-serif;color:var(--ink);position:relative}
.spread{position:absolute;left:24px;width:800px;height:530px;background:var(--paper);overflow:hidden;box-shadow:0 6px 18px rgba(0,0,0,.35)}
.spread--inside{top:34px}
.spread--outside{top:634px}
.band{position:absolute;left:0;width:800px}
.panel{position:absolute;top:0;width:266.67px;height:530px}
.panel--1{left:0}.panel--2{left:266.67px}.panel--3{left:533.33px}
.fold{position:absolute;top:0;width:1px;height:530px;background:rgba(0,0,0,.07)}
.photo{position:absolute;background:linear-gradient(135deg,#b49a7c,#6e5a48)}
.photo--round{border-radius:50%;border:5px solid #fff;box-shadow:0 0 0 3px var(--teal)}
h2.section{font-weight:800;font-size:13px;color:var(--rust);letter-spacing:.2px}
h3.sub{font-weight:700;font-size:11px;color:var(--plum)}
p.copy{font-size:8.2px;line-height:1.42;margin-top:6px}
p.copy b{font-weight:700}
.text{position:absolute}
.brand{position:absolute;display:flex;align-items:center;gap:6px;font-weight:600;font-size:13px;color:#fff}
.brand .dot{width:14px;height:14px;border-radius:50%;background:#fff;flex:none}
.fees{margin-top:8px;display:grid;grid-template-columns:1fr 1fr;border:1px solid var(--fee-line);background:var(--fee)}
.fees span{font-size:7.3px;padding:4px 5px;border-bottom:1px solid var(--fee-line);border-right:1px solid var(--fee-line)}
.fees span:nth-child(2n){border-right:none}
.fees span:nth-last-child(-n+2){border-bottom:none}
.fees-title{margin-top:12px;text-align:center;font-weight:700;font-size:11px;color:var(--rust)}
.contact{position:absolute;font-size:8.5px;line-height:1.45;color:#fff}
.contact strong{display:block;font-size:12px;font-weight:800;color:#fff;margin-bottom:2px}
.sub--teal{color:var(--teal-dark);font-size:10px;font-weight:700}
.closing{position:absolute;color:#e6e6e6;font-size:8px;line-height:1.45;font-style:italic}
</style>
</head>
<body>

<!-- Inside spread -->
<section class="spread spread--inside" aria-label="Brochure inside spread">
  <svg class="band" style="top:0" width="800" height="90" viewBox="0 0 800 90" aria-hidden="true">
    <path d="M0 0H800V70C700 74 620 40 530 52C440 64 380 40 300 50C220 60 120 40 0 58Z" fill="var(--sand)"/>
    <path d="M0 0H800V60C700 64 620 32 530 44C440 56 380 32 300 42C220 52 120 32 0 50Z" fill="var(--teal)"/>
  </svg>
  <svg class="band" style="top:430px" width="800" height="100" viewBox="0 0 800 100" aria-hidden="true">
    <path d="M0 30C150 10 300 50 450 30C600 12 700 34 800 20V100H0Z" fill="var(--sand)"/>
    <path d="M0 40C150 20 300 60 450 40C600 22 700 44 800 30V100H0Z" fill="var(--plum)"/>
  </svg>
  <div class="fold" style="left:266px"></div><div class="fold" style="left:533px"></div>

  <div class="panel panel--1">
    <div class="photo photo--round" style="left:18px;top:14px;width:118px;height:118px;background:linear-gradient(135deg,#c9b291,#7a6247)" role="img" aria-label="Photo of the home's bright living room with sofas"></div>
    <div class="text" style="left:20px;top:150px;width:228px">
      <h2 class="section">OUR SERVICES</h2>
      <p class="copy"><b>Harlow Senior Living</b> is a unique care concept, designed around a social model which encourages <b>"neighbors"</b> to be as independent as possible, actively participate in life here, and interact with their fellow neighbors.</p>
      <p class="copy">Here, you'll maintain purpose in life while having personal care assistance as needed, activities, exercise, transportation, and companionship. Professional staff will be in residence 24 hours a day. This is a very special home, offering you a loving and nurturing life experience.</p>
      <p class="copy">Stay busy doing what you love here! Participate in as many activities as you like and discover life anew. Keep up your favorite hobbies or take up new ones.</p>
    </div>
    <div class="brand" style="left:22px;top:488px"><span class="dot"></span>Harlow Senior Living</div>
  </div>

  <div class="panel panel--2">
    <div class="text" style="left:18px;top:70px;width:230px">
      <p class="copy">In our home, neighbors can do a little gardening, stay in touch with family and friends on social media, email, or by video call, relax in the soaking tub, take up a new hobby, enjoy music and crafts, community outings, exercise programs, beach walks, movie nights, board games, barbecues, and a whole lot more.</p>
      <p class="copy"><b>Harlow Senior Living</b> is a home where neighbors are actively engaged, individuality is encouraged, and life has purpose. It's a home!</p>
      <p class="copy">Make it <b>your</b> home, today!</p>
      <p class="fees-title">Monthly fees include:</p>
      <div class="fees">
        <span>3 daily meals + snacks</span><span>Accommodations</span>
        <span>Activities</span><span>Medication Management</span>
        <span>Laundry</span><span>Care Planning</span>
        <span>Housekeeping</span><span>Regular Nursing Visits</span>
        <span>Utilities</span><span>Access to Staff 24/7</span>
      </div>
    </div>
  </div>

  <div class="panel panel--3">
    <div class="photo photo--round" style="left:120px;top:8px;width:112px;height:112px;background:linear-gradient(135deg,#b8a282,#5d4a38)" role="img" aria-label="Photo of a furnished common room"></div>
    <div class="text" style="left:18px;top:138px;width:232px">
      <h3 class="sub">Lifestyle Support</h3>
      <p class="copy">For neighbors who are relatively independent but might benefit from lifestyle support, with assistance as needed, medication management, access to staff 24/7, and regular nursing visits.</p>
      <h3 class="sub" style="margin-top:10px">Personal Care</h3>
      <p class="copy">Hands-on care: Daily bathing, dressing, toileting, incontinence care, grooming, assistance with ambulation, transfers, range of motion exercises, verbal cueing, medication management, &amp; feeding.</p>
    </div>
    <div class="photo photo--round" style="left:130px;top:300px;width:118px;height:118px;background:linear-gradient(135deg,#e6dfcf,#b8a98a)" role="img" aria-label="Photo of an accessible bathroom"></div>
  </div>
</section>

<!-- Outside spread -->
<section class="spread spread--outside" aria-label="Brochure outside spread">
  <svg class="band" style="top:0" width="800" height="530" viewBox="0 0 800 530" aria-hidden="true">
    <path d="M0 440C180 400 420 470 800 420V530H0Z" fill="var(--slate)"/>
    <path d="M560 0H800V360C740 250 660 170 560 130Z" fill="var(--teal)"/>
  </svg>
  <div class="fold" style="left:266px"></div><div class="fold" style="left:533px"></div>

  <div class="panel panel--1">
    <div class="photo" style="left:18px;top:18px;width:230px;height:150px;border:4px solid #fff;background:linear-gradient(135deg,#d99a86,#6f8fa6)" role="img" aria-label="Photo of two smiling senior women sharing a drink"></div>
    <div class="text" style="left:20px;top:184px;width:228px">
      <h2 class="section">FAMILY CENTER</h2>
      <p class="sub--teal">An Education Resource for Families</p>
      <p class="copy">Harlow Care Group is proud to offer an innovative educational resource to help you better understand the aging and long-term care processes.</p>
      <p class="copy">Introducing the Family Series, a selection of online training courses designed to provide knowledge and guidance for family members. The courses enable you to be part of the treatment team and ensure that your loved one(s) get the highest quality of care.</p>
      <p class="copy">Understanding the aging process and its complexities can be overwhelming. Knowing what to expect and how to support your loved one's changing needs is critical. The courses included in the Family Series provide a wealth of information on a broad range of topics, allowing us to enrich the care that we provide while working in tandem with your expectations.</p>
    </div>
    <p class="closing" style="left:20px;top:466px;width:226px">Family members play a critical role in the success of Harlow Senior Living. We hope that this additional resource will provide an exceptional tool and a valuable service, and strengthen our partnership with you.</p>
  </div>

  <div class="panel panel--2">
    <div class="text" style="left:18px;top:18px;width:230px">
      <h2 class="section">About Harlow Senior Living</h2>
      <p class="copy">Harlow Care Group is proud to usher in a new era in long-term care. Harlow Senior Living was developed as a solution to increasing requests from our clients for assistance locating suitable homes or facilities when in-home care is no longer appropriate. Now, your care can remain with the best!</p>
      <p class="copy">Harlow Senior Living Lakeside is a brand new state of the art home located in Lakeside at 96 Meadow Bay Drive. Up to 22 "neighbors" enjoy this 11,000 square foot home with 19 fully furnished private rooms with private bathrooms. Room sizes range from 180 to 225 sq ft. Each has a flat screen TV, artwork, electric bed, desk, chair, dressers, mirrored doors, built-in closet system, and ceiling fan, plus an independent air conditioner.</p>
    </div>
    <div class="photo" style="left:26px;top:254px;width:214px;height:120px;border:4px solid #fff;background:linear-gradient(180deg,#7fb2dc 0%,#b7d3ea 40%,#c58a62 41%,#9a6a4c 100%)" role="img" aria-label="Photo of the two-storey residence exterior"></div>
    <div class="contact" style="left:26px;top:430px;width:220px">
      <strong>Harlow Senior Living</strong>
      450 Harbor View Rd., Suite 210<br>Lakeside, ST 00000<br>
      (555) 010-4486<br>Fax (555) 010-4822<br>info@harlowcare.example<br>www.harlowcare.example
    </div>
  </div>

  <div class="panel panel--3">
    <div class="photo" style="left:0;top:0;width:266.67px;height:340px;border-bottom-right-radius:100% 40%;background:linear-gradient(160deg,#c9d6e4 0%,#8e9fb4 45%,#3e4a6b 100%)" role="img" aria-label="Photo of a smiling senior couple embracing"></div>
    <div class="brand" style="left:120px;top:372px;color:var(--teal-dark)"><span class="dot" style="background:var(--teal)"></span>Harlow Senior Living</div>
  </div>
</section>

</body>
</html>
```